Modern Billboard Ad for Criminal Defense Firm

10.5 x 36 We're looking for something to set us apart from the local competition. Looking for sleek and modern. We're a mid-sized firm in a small market city. We want to give the artist room to be creative on this one.
Thanks

Target Market(s)

Adult clients who have been charged with a crime/DWI

Industry/Entity Type

legal

Font styles to use
Serif
Sans Serif

Requirements
Must have
• Needs to have the firm name in large lettering. Law Offices of Marcus T Whitfield. “PLLC” does not have to be included. Phone number of (555) 384-1927 should be included but not the main focus.
Nice to have
• A call to action or something similar. “Don’t go it alone, call today.”, “ Arrested?”

```html
<!DOCTYPE html>
<html lang="en">
<head>
<meta charset="utf-8">
<title>Marcus T Whitfield Billboard</title>
<link href="https://fonts.googleapis.com/css2?family=DM+Serif+Display&family=Montserrat:wght@500;700;800&display=swap" rel="stylesheet">
<style>
  :root {
    --page: #e9ecef;
    --navy-deep: #0b1a30;
    --navy: #16294a;
    --navy-light: #1f3a63;
    --white: #ffffff;
    --blue: #1e7fd6;
    --blue-text: #3a8fe0;
    --red: #f2111a;
    --portrait-light: #b9b9b9;
    --portrait-dark: #3b3d42;
  }
  * { margin: 0; padding: 0; box-sizing: border-box; }
  html, body {
    width: 1200px; height: 900px; overflow: hidden;
    background: var(--page);
  }
  .billboard {
    position: absolute;
    left: 40px; top: 287px;
    width: 1120px; height: 327px;
    background: linear-gradient(100deg, var(--navy-light) 0%, var(--navy) 40%, var(--navy-deep) 100%);
    overflow: hidden;
    font-family: "Montserrat", sans-serif;
    color: var(--white);
  }
  .portrait {
    position: absolute;
    left: 0; top: 0;
    width: 345px; height: 100%;
    background: linear-gradient(90deg, var(--portrait-dark) 0%, var(--portrait-light) 45%, var(--portrait-dark) 85%, rgba(22,41,74,0) 100%);
  }
  .eyebrow {
    position: absolute;
    left: 380px; width: 700px; top: 30px;
    display: flex; align-items: center; justify-content: center; gap: 22px;
    font-weight: 500; font-size: 24px; letter-spacing: 7px;
    white-space: nowrap;
  }
  .eyebrow .rule { width: 90px; height: 2px; background: var(--blue); }
  .firm-name {
    position: absolute;
    left: 360px; width: 740px; top: 72px;
    text-align: center;
    font-family: "DM Serif Display", serif;
    font-size: 80px; line-height: 1; font-weight: 400;
    letter-spacing: 1px;
    white-space: nowrap;
  }
  .cta-box {
    position: absolute;
    left: 330px; top: 188px;
    width: 250px; height: 72px;
    background: var(--blue);
    display: flex; flex-direction: column; justify-content: center;
    padding-left: 18px;
    font-weight: 800; text-transform: uppercase; line-height: 1.05;
    white-space: nowrap;
  }
  .cta-box .small { font-size: 17px; }
  .cta-box .large { font-size: 26px; }
  .arrested-band {
    position: absolute;
    left: 580px; top: 196px;
    width: 540px; height: 84px;
    background: var(--red);
    display: flex; align-items: center;
    padding-left: 18px;
    font-weight: 800; font-size: 68px; letter-spacing: 1px;
    white-space: nowrap;
  }
  .contact {
    position: absolute;
    left: 430px; top: 284px;
    font-size: 22px; letter-spacing: 4px; font-weight: 500;
    white-space: nowrap;
  }
  .contact .label { color: var(--blue-text); font-weight: 700; margin-right: 10px; }
  .award-badge {
    position: absolute;
    left: 1058px; top: 242px;
    width: 50px; height: 74px;
    background: var(--blue);
    border: 2px solid var(--white);
  }
</style>
</head>
<body>
  <div class="billboard">
    <div class="portrait" role="img" aria-label="Black and white portrait of the attorney in a suit and vest"></div>

    <div class="eyebrow"><span class="rule"></span><span>LAW OFFICES OF</span><span class="rule"></span></div>
    <h1 class="firm-name">Marcus T Whitfield</h1>

    <div class="cta-box">
      <span class="small">Don’t go it alone,</span>
      <span class="large">Call today.</span>
    </div>

    <div class="arrested-band">ARRESTED?</div>

    <p class="contact"><span class="label">CALL US:</span>(555) 384-1927</p>

    <div class="award-badge" role="img" aria-label="Award badge"></div>
  </div>
</body>
</html>
```